Lone Willow Estate Vault Reserve Wine Label (Front and Back)

I need to create an elite tier wine label.  I would like it to be in a light, natural color with silver or gold.  I would like it to look rich and expensive, mostly monochromatic, elegantly simple.  It will need to stand up next to wine labels that are black and charcoal colored and look like the more expensive wine of the 3.  I have attached a similar label that it will be grouped with and some instructions.
We are a winery in southeast Washington state with a reputation for fine wines and top notch terroir.  We want to present family, tradition and high value wine in the bottle.

```html
<!DOCTYPE html>
<html lang="en">
<head>
<meta charset="utf-8">
<title>Lone Willow Estate – Vault Reserve Label</title>
<link href="https://fonts.googleapis.com/css2?family=Cinzel:wght@400;700&family=EB+Garamond:wght@400;500&family=Great+Vibes&display=swap" rel="stylesheet">
<style>
  :root {
    --backdrop: #e8e8e9;
    --paper: #f3f4f6;
    --paper-shade: #e4e6e9;
    --ink: #141414;
    --gold-dark: #a86f1c;
    --gold: #c9953a;
    --gold-light: #f4e4b0;
  }
  html, body {
    margin: 0;
    padding: 0;
    width: 1200px;
    height: 1191px;
    overflow: hidden;
    background: var(--backdrop);
  }
  .label {
    position: absolute;
    left: 278px;
    top: 90px;
    width: 644px;
    height: 1010px;
    background: linear-gradient(135deg, var(--paper) 0%, #ffffff 45%, var(--paper-shade) 100%);
    box-shadow: 0 2px 10px rgba(0,0,0,0.08);
    color: var(--ink);
    text-align: center;
  }
  .label > * { position: absolute; left: 0; right: 0; margin: 0; }
  .estate-name {
    top: 92px;
    font-family: "Cinzel", serif;
    font-weight: 400;
    font-size: 64px;
    line-height: 88px;
    letter-spacing: 1px;
  }
  .region {
    top: 306px;
    font-family: "EB Garamond", serif;
    font-weight: 500;
    font-size: 27px;
    letter-spacing: 7px;
  }
  .name-mark {
    top: 379px;
    left: 213px;
    right: auto;
    width: 218px;
    height: 233px;
    box-sizing: border-box;
    border: 4px solid var(--gold);
    display: flex;
    align-items: center;
    justify-content: center;
    font-family: "Cinzel", serif;
    font-weight: 400;
    font-size: 26px;
    line-height: 38px;
    color: var(--gold);
  }
  .vineyard {
    top: 646px;
    font-family: "EB Garamond", serif;
    font-size: 28px;
    letter-spacing: 1px;
  }
  .tier {
    top: 700px;
    font-family: "Cinzel", serif;
    font-weight: 700;
    font-size: 56px;
    letter-spacing: 1px;
    text-shadow: 3px 2px 0 var(--gold);
  }
  .varietal {
    top: 782px;
    font-family: "Great Vibes", cursive;
    font-size: 48px;
    color: var(--gold-dark);
  }
  .vintage {
    top: 872px;
    font-family: "EB Garamond", serif;
    font-size: 26px;
  }
  .heritage-band {
    top: 945px;
    left: 20px;
    right: 20px;
    height: 63px;
    display: flex;
    align-items: center;
    justify-content: center;
    background: linear-gradient(90deg, var(--gold-dark) 0%, var(--gold) 25%, var(--gold-light) 50%, var(--gold) 75%, var(--gold-dark) 100%);
    font-family: "EB Garamond", serif;
    font-weight: 500;
    font-size: 21px;
    color: var(--ink);
  }
</style>
</head>
<body>
  <div class="label">
    <h1 class="estate-name">LONE WILLOW<br>ESTATE</h1>
    <p class="region">HORSE HEAVEN HILLS</p>
    <div class="name-mark">LONE<br>WILLOW<br>ESTATE</div>
    <p class="vineyard">ESTATE VINEYARD</p>
    <p class="tier">VAULT RESERVE</p>
    <p class="varietal">Cabernet Sauvignon</p>
    <p class="vintage">2022</p>
    <p class="heritage-band">FAMILY STEWARDS OF THE LAND FOR 5 GENERATIONS</p>
  </div>
</body>
</html>
```